Offshore Energy Projects Management Consultancy needs a business card design

Logo available. We provide teams to deliver engineering consultancy, project management and delivery teams mainly in the offshore renewables sector. The company is all about bringing the right people to a project to deliver the scope.

The business card will be used for all staff.

The business card should be quite simple, vibrant and uncluttered but convey experience, enthusiasm and integration.

Target Market(s)

Energy Project Developers and Tier 1 construction companies

Contact Information for Business Card

Logo should be on the back of the card. I'm happy for the designer to play with the colour of the logo and background colour.

Front of the card should convey all the must have information in a clear and professional manner but without being overly traditional.

Colors

Designer to choose colors to be used in the design.

Requirements
Must have
• Land Line Tel Number, Mobile Tel Number, Email, business address, web address.

```html
<!DOCTYPE html>
<html lang="en">
<head>
<meta charset="utf-8">
<title>Tidewater Delivery Group – Business Card</title>
<link rel="stylesheet" href="https://fonts.googleapis.com/css2?family=Montserrat:wght@400;500;600;700&display=swap">
<style>
  :root {
    --stage: #2b2d31;
    --card-white: #ffffff;
    --card-grey: #6b6c70;
    --ring-grey: #55565a;
    --blue-deep: #1368b8;
    --blue-mid: #1f8ad6;
    --blue-bright: #25a6e3;
    --text-grey: #5d5f63;
    --text-dark: #4a4c50;
  }
  * { box-sizing: border-box; margin: 0; padding: 0; }
  html, body { width: 1200px; height: 900px; overflow: hidden; }
  body {
    background: var(--stage);
    font-family: "Montserrat", sans-serif;
    position: relative;
  }
  .card {
    position: absolute;
    overflow: hidden;
    border-radius: 4px;
    box-shadow: 0 14px 30px rgba(0,0,0,0.45);
  }
  .card-art { position: absolute; inset: 0; }

  /* Back of card (portrait, grey) */
  .card-back {
    left: 110px; top: 170px;
    width: 330px; height: 570px;
    background: var(--card-grey);
  }
  .back-brand {
    position: absolute;
    left: 0; right: 0; top: 375px;
    text-align: center;
    color: var(--card-white);
  }
  .back-brand .brand-name {
    font-weight: 700;
    font-size: 25px;
    letter-spacing: 0.5px;
    line-height: 1.15;
    text-transform: uppercase;
  }
  .back-brand .brand-mark {
    display: block;
    width: 14px; height: 14px;
    margin: 0 auto 16px;
    background: var(--card-white);
    border-radius: 50%;
  }

  /* Front of card (landscape, white) */
  .card-front {
    left: 500px; top: 255px;
    width: 620px; height: 360px;
    background: var(--card-white);
  }
  .front-content {
    position: absolute;
    left: 40px; top: 36px;
    width: 360px;
  }
  .front-brand {
    font-weight: 700;
    font-size: 17px;
    color: var(--text-dark);
    text-transform: uppercase;
    letter-spacing: 0.4px;
  }
  .person-name {
    margin-top: 22px;
    font-weight: 700;
    font-size: 22px;
    color: var(--blue-deep);
  }
  .person-role {
    font-weight: 500;
    font-size: 15px;
    color: var(--blue-bright);
    margin-top: 2px;
  }
  .divider {
    width: 16px; height: 2px;
    background: var(--text-grey);
    margin: 12px 0 10px;
  }
  .contact-list { list-style: none; }
  .contact-list li {
    display: flex; align-items: center; gap: 10px;
    font-size: 14.5px;
    color: var(--text-grey);
    line-height: 24px;
  }
  .contact-list svg { width: 14px; height: 14px; flex: none; }
  .address {
    margin-top: 18px;
    font-size: 15px;
    font-weight: 500;
    color: var(--blue-bright);
    line-height: 1.35;
  }
</style>
</head>
<body>

<section class="card card-back" aria-label="Card back">
  <svg class="card-art" viewBox="0 0 330 570" aria-hidden="true">
    <defs>
      <radialGradient id="backBlue" cx="50%" cy="30%" r="70%">
        <stop offset="0" stop-color="var(--blue-bright)"/>
        <stop offset="1" stop-color="var(--blue-deep)"/>
      </radialGradient>
    </defs>
    <circle cx="165" cy="60" r="232" fill="var(--blue-bright)"/>
    <circle cx="165" cy="60" r="220" fill="var(--card-grey)"/>
    <circle cx="165" cy="60" r="212" fill="var(--ring-grey)"/>
    <circle cx="165" cy="60" r="204" fill="url(#backBlue)"/>
  </svg>
  <div class="back-brand">
    <span class="brand-mark"></span>
    <div class="brand-name">Tidewater<br>Delivery Group</div>
  </div>
</section>

<section class="card card-front" aria-label="Card front">
  <svg class="card-art" viewBox="0 0 620 360" aria-hidden="true">
    <defs>
      <radialGradient id="frontBlue" cx="30%" cy="45%" r="75%">
        <stop offset="0" stop-color="var(--blue-bright)"/>
        <stop offset="1" stop-color="var(--blue-deep)"/>
      </radialGradient>
    </defs>
    <circle cx="650" cy="245" r="232" fill="var(--blue-bright)"/>
    <circle cx="650" cy="245" r="220" fill="var(--card-white)"/>
    <circle cx="650" cy="245" r="212" fill="url(#frontBlue)"/>
  </svg>
  <div class="front-content">
    <div class="front-brand">Tidewater Delivery Group</div>
    <div class="person-name">Marek Ostrowski</div>
    <div class="person-role">Managing Director</div>
    <div class="divider"></div>
    <ul class="contact-list">
      <li>
        <svg viewBox="0 0 16 16"><path d="M4 1.5l2.5 3-1.5 1.5a8 8 0 0 0 5 5l1.5-1.5 3 2.5-1.5 2.5C7 14 2 9 1.5 3z" fill="none" stroke="var(--blue-bright)" stroke-width="1.4"/></svg>
        +44 000 555 0142
      </li>
      <li>
        <svg viewBox="0 0 16 16"><rect x="4" y="1" width="8" height="14" rx="1.5" fill="none" stroke="var(--blue-bright)" stroke-width="1.4"/><circle cx="8" cy="12.5" r="0.9" fill="var(--blue-bright)"/></svg>
        +44 000 555 0187
      </li>
      <li>
        <svg viewBox="0 0 16 16"><rect x="1" y="3" width="14" height="10" rx="1" fill="none" stroke="var(--blue-bright)" stroke-width="1.4"/><path d="M1.5 3.5L8 9l6.5-5.5" fill="none" stroke="var(--blue-bright)" stroke-width="1.4"/></svg>
        info@tidewaterdelivery.uk
      </li>
      <li>
        <svg viewBox="0 0 16 16"><circle cx="8" cy="8" r="7" fill="var(--blue-bright)"/><path d="M1 8h14M8 1c-3 3.5-3 10.5 0 14M8 1c3 3.5 3 10.5 0 14" fill="none" stroke="var(--card-white)" stroke-width="1"/></svg>
        www.tidewaterdelivery.uk
      </li>
    </ul>
    <p class="address">18 Harbour Quay Road<br>Aberdeen AB11 5QE</p>
  </div>
</section>

</body>
</html>
```